wine bottle label design

My girlfriend and I are getting married. We are sending out invitations, in a wine bottle. For that we need a label on the bottle.
Our names are Mette & Jørgen. We would like the M and J to somehow play a bigger part in the logo.
Also maybe with an Illustration (best if made as a drawing resembling the church we are getting married in) https://www.fjordtonerne.dk/index.php/kalender/83-uncategorised/148-gospelgudstjeneste-i-dalbro-kirke.html

Bryllup den 27 april 2019, kl. 14:00 i Dalbro Kirke

Decorative

```html
<!DOCTYPE html>
<html lang="da">
<head>
<meta charset="utf-8">
<title>Bryllup – Mette &amp; Jørgen – vinetiket</title>
<link href="https://fonts.googleapis.com/css2?family=Great+Vibes&family=Alegreya+Sans+SC:wght@500&display=swap" rel="stylesheet">
<style>
  :root {
    --page: #f6f6f6;
    --rose-light: #f2b8a8;
    --rose: #ea9a86;
    --rose-deep: #e0826c;
    --wine: #8a1218;
    --lace: rgba(255, 255, 255, 0.6);
    --band: rgba(255, 240, 236, 0.85);
    --church-warm: #eeb27a;
    --church-roof: #c9644a;
    --church-green: #b59a3c;
  }
  html, body {
    margin: 0;
    width: 1200px;
    height: 1200px;
    overflow: hidden;
    background: var(--page);
  }
  .label {
    position: absolute;
    left: 240px;
    top: 50px;
    width: 720px;
    height: 1100px;
    background: linear-gradient(90deg, var(--rose-light) 0%, var(--rose) 45%, var(--rose-deep) 100%);
    overflow: hidden;
  }
  .lace-heart {
    position: absolute;
    left: 0;
    top: 0;
    width: 720px;
    height: 620px;
  }
  .church-scene {
    position: absolute;
    left: 0;
    top: 380px;
    width: 720px;
    height: 605px;
  }
  .names {
    position: absolute;
    left: 0;
    top: 0;
    width: 720px;
    height: 620px;
    color: var(--wine);
  }
  .name {
    position: absolute;
    font-family: "Alegreya Sans SC", sans-serif;
    font-weight: 500;
    font-size: 70px;
    letter-spacing: 2px;
    line-height: 1;
    white-space: nowrap;
  }
  .name .initial {
    font-family: "Great Vibes", cursive;
    font-weight: 400;
    font-size: 190px;
    letter-spacing: 0;
    vertical-align: -24px;
  }
  .name--bride { left: 110px; top: 100px; }
  .name--bride .initial { margin-right: 4px; }
  .name--groom { left: 150px; top: 340px; }
  .name--groom .initial { margin-right: 28px; }
  .ampersand {
    position: absolute;
    left: 255px;
    top: 270px;
    font-family: "Great Vibes", cursive;
    font-size: 64px;
    line-height: 1;
  }
  .wedding-date {
    position: absolute;
    left: 340px;
    top: 640px;
    width: 350px;
    margin: 0;
    text-align: center;
    color: var(--wine);
    font-family: "Great Vibes", cursive;
    font-size: 54px;
    line-height: 1.15;
  }
  .wedding-date .day { display: block; }
  .time-band {
    position: absolute;
    left: 0;
    top: 985px;
    width: 720px;
    height: 115px;
    background: var(--band);
    display: flex;
    align-items: center;
    justify-content: center;
    color: var(--wine);
    font-family: "Alegreya Sans SC", sans-serif;
    font-weight: 500;
    font-size: 54px;
    letter-spacing: 1px;
  }
</style>
</head>
<body>
  <main class="label">
    <svg class="church-scene" viewBox="0 0 720 605" preserveAspectRatio="none" role="img" aria-label="Tegning af Dalbro Kirke med tårn, skib og grønt landskab">
      <defs>
        <linearGradient id="sceneTone" x1="0" y1="0" x2="1" y2="0">
          <stop offset="0%" stop-color="var(--church-warm)"/>
          <stop offset="55%" stop-color="var(--church-roof)"/>
          <stop offset="100%" stop-color="var(--church-green)"/>
        </linearGradient>
        <linearGradient id="sceneFade" x1="0" y1="0" x2="0" y2="1">
          <stop offset="0%" stop-color="#fff" stop-opacity="0"/>
          <stop offset="55%" stop-color="#fff" stop-opacity="0.6"/>
          <stop offset="100%" stop-color="#fff" stop-opacity="1"/>
        </linearGradient>
        <mask id="sceneMask">
          <rect width="720" height="605" fill="url(#sceneFade)"/>
        </mask>
      </defs>
      <rect width="720" height="605" fill="url(#sceneTone)" mask="url(#sceneMask)"/>
    </svg>

    <svg class="lace-heart" viewBox="0 0 720 620" role="img" aria-label="Hvidt kniplingshjerte som ramme om navnene">
      <defs>
        <radialGradient id="heartGlow" cx="50%" cy="40%" r="60%">
          <stop offset="0%" stop-color="#ffffff" stop-opacity="0.6"/>
          <stop offset="100%" stop-color="#ffffff" stop-opacity="0.25"/>
        </radialGradient>
      </defs>
      <path d="M360 120 C300 10 40 20 20 190 C0 330 200 460 360 600 C520 460 720 330 700 190 C680 20 420 10 360 120 Z"
            fill="url(#heartGlow)" stroke="var(--lace)" stroke-width="10"/>
    </svg>

    <div class="names">
      <div class="name name--bride"><span class="initial">M</span>ETTE</div>
      <div class="ampersand">&amp;</div>
      <div class="name name--groom"><span class="initial">J</span>ØRGEN</div>
    </div>

    <p class="wedding-date">Bryllup den<span class="day">27 april 2019</span></p>

    <div class="time-band">kl. 14:00 i Dalbro Kirke</div>
  </main>
</body>
</html>
```